Visitenkarte erstellen für Reiki Praxis

Visitenkarten für Reiki Praxis Doppelseitig

business cards reiki practice double-sided

The background can also be a different color

```html
<!DOCTYPE html>
<html lang="en">
<head>
<meta charset="utf-8">
<title>Calm River Reiki – Business Cards</title>
<link href="https://fonts.googleapis.com/css2?family=Outfit:wght@300;400;500;700&display=swap" rel="stylesheet">
<style>
  :root {
    --page-bg: #ece9ee;
    --card-purple: #5a0070;
    --gold-light: #f4e07c;
    --gold-mid: #e2b93a;
    --gold-deep: #c48c0c;
    --gold-line: #d9aa3c;
    --text-white: #ffffff;
    --card-shadow: rgba(40, 10, 50, 0.28);
  }
  * { box-sizing: border-box; margin: 0; padding: 0; }
  html, body {
    width: 1200px; height: 800px; overflow: hidden;
    background: var(--page-bg);
    font-family: "Outfit", sans-serif;
  }
  .canvas { position: relative; width: 1200px; height: 800px; }
  .card {
    position: absolute; top: 125px;
    width: 330px; height: 550px;
    border-radius: 24px;
    background: var(--card-purple);
    overflow: hidden;
    box-shadow: 8px 10px 22px var(--card-shadow);
  }
  .card--back { left: 242px; }
  .card--front { left: 628px; }

  /* back */
  .back-mark {
    position: absolute; left: 0; right: 0; top: 372px;
    display: flex; align-items: center; justify-content: center; gap: 7px;
    color: var(--gold-mid); font-weight: 400; font-size: 12px; letter-spacing: 1.5px;
  }
  .back-mark .dot { width: 10px; height: 10px; border-radius: 50%; background: var(--gold-mid); }

  /* front */
  .centered { position: absolute; left: 0; right: 0; text-align: center; color: var(--text-white); }
  .brand-dot {
    position: absolute; left: 50%; top: 44px; width: 40px; height: 40px; margin-left: -20px;
    border-radius: 50%; border: 2px solid var(--gold-mid);
  }
  .brand-name { top: 92px; font-size: 19px; font-weight: 300; letter-spacing: 0.6px; }
  .brand-owner { top: 118px; font-size: 12px; font-weight: 300; letter-spacing: 4px; color: var(--gold-mid); }
  .person-name { top: 151px; font-size: 25px; font-weight: 700; letter-spacing: 0.5px; line-height: 1; }
  .person-role { top: 179px; font-size: 13px; font-weight: 500; }
  .divider {
    position: absolute; left: 62px; width: 206px; top: 201px; height: 1.5px; background: var(--text-white);
  }
  .divider::after {
    content: ""; position: absolute; left: 74px; top: -0.5px; width: 58px; height: 3px;
    background: var(--gold-deep); border-radius: 2px;
  }
  .contact-icon { position: absolute; left: 50%; margin-left: -6px; width: 12px; height: 12px; }
  .icon-pin { top: 210px; height: 14px; }
  .icon-phone { top: 262px; }
  .icon-mail { top: 297px; }
  .contact-text { font-size: 13px; font-weight: 400; line-height: 15px; }
  .contact-address { top: 227px; }
  .contact-phone { top: 280px; }
  .contact-email { top: 312px; }

  .card-base { position: absolute; left: 0; top: 0; width: 330px; height: 550px; }
  .lotus-area {
    position: absolute; left: 71px; top: 347px; width: 188px; height: 178px;
    border-radius: 50% 50% 40% 40%;
    background: radial-gradient(ellipse at 50% 55%, rgba(226, 185, 58, 0.32), rgba(90, 0, 112, 0.15) 70%);
  }
</style>
</head>
<body>
<div class="canvas">

  <section class="card card--back" aria-label="Card back">
    <div class="back-mark"><span class="dot"></span>CALM RIVER REIKI</div>
  </section>

  <section class="card card--front" aria-label="Card front">
    <svg class="card-base" viewBox="0 0 330 550" aria-hidden="true">
      <defs>
        <linearGradient id="goldFill" x1="0" y1="0" x2="1" y2="1">
          <stop offset="0" stop-color="#f4e07c"/>
          <stop offset="0.55" stop-color="#e2b93a"/>
          <stop offset="1" stop-color="#c48c0c"/>
        </linearGradient>
      </defs>
      <path d="M0,440 C45,448 75,500 120,518 C150,530 180,530 210,518 C255,500 285,448 330,440 L330,550 L0,550 Z" fill="url(#goldFill)"/>
      <path d="M0,425 C60,395 110,445 165,500 C220,445 270,395 330,425" fill="none" stroke="#d9aa3c" stroke-width="2"/>
    </svg>

    <div class="lotus-area" role="img" aria-label="Gold line-art lotus flower decoration"></div>

    <span class="brand-dot"></span>
    <p class="centered brand-name">CALM RIVER REIKI</p>
    <p class="centered brand-owner">MARA LINDQVIST</p>

    <h1 class="centered person-name">JOHN DOE</h1>
    <p class="centered person-role">Manager</p>
    <div class="divider"></div>

    <svg class="contact-icon icon-pin" viewBox="0 0 12 14" aria-hidden="true">
      <path d="M6 1 C3.2 1 1.5 3 1.5 5.2 C1.5 8 6 12 6 12 C6 12 10.5 8 10.5 5.2 C10.5 3 8.8 1 6 1 Z" fill="none" stroke="#e2b93a" stroke-width="1.4"/>
      <circle cx="6" cy="5.2" r="1.6" fill="#e2b93a"/>
      <line x1="2.5" y1="13.2" x2="9.5" y2="13.2" stroke="#e2b93a" stroke-width="1.2"/>
    </svg>
    <p class="centered contact-text contact-address">Your Address, Your<br>City,box88900</p>

    <svg class="contact-icon icon-phone" viewBox="0 0 12 12" aria-hidden="true">
      <circle cx="6" cy="6" r="6" fill="#e2b93a"/>
      <path d="M3.8 3.2 L4.9 3 L5.5 4.6 L4.8 5.2 C5.2 6.1 5.9 6.8 6.8 7.2 L7.4 6.5 L9 7.1 L8.8 8.2 C6 8.4 3.6 6 3.8 3.2 Z" fill="#5a0070"/>
    </svg>
    <p class="centered contact-text contact-phone">111-222-333</p>

    <svg class="contact-icon icon-mail" viewBox="0 0 12 12" aria-hidden="true">
      <circle cx="6" cy="6" r="6" fill="#e2b93a"/>
      <rect x="3" y="4" width="6" height="4.2" fill="none" stroke="#5a0070" stroke-width="0.9"/>
      <path d="M3 4 L6 6.4 L9 4" fill="none" stroke="#5a0070" stroke-width="0.9"/>
    </svg>
    <p class="centered contact-text contact-email">info@calmriverreiki.com</p>
  </section>

</div>
</body>
</html>
```